sommelier *

Sommelier Wine Hospitality Tavergne Crest experience I'm working as a sommelier in a Tavergne Crest restaurant. I try to reach People who are interested in invest in wine and wine loovers! In terms of color I would like to have a nice color based on a nice bordeaux red (as an advice). By the way i forgot to write my phone number and my email address. 438271905316 kdorvan4@quillpost.net I hope this info is enough so far.

```html
<!DOCTYPE html>
<html lang="en">
<head>
<meta charset="utf-8">
<title>Lorenz Hadwiger – Sommelier Business Card</title>
<link href="https://fonts.googleapis.com/css2?family=Josefin+Slab:wght@600;700&display=swap" rel="stylesheet">
<style>
  :root {
    --backdrop: #6e5b48;
    --coral-light: #f6b09a;
    --coral: #f3967c;
    --coral-deep: #ee8567;
    --ink: #1c1412;
    --card-black: #050505;
    --white: #f4f1ee;
    --bordeaux: #8e1b1f;
    --wine: #7a1630;
    --wood: #6a3a1c;
  }
  * { margin: 0; padding: 0; box-sizing: border-box; }
  html, body {
    width: 900px;
    height: 1200px;
    overflow: hidden;
    background: var(--backdrop);
  }
  .canvas {
    position: relative;
    width: 900px;
    height: 1200px;
    font-family: "Josefin Slab", Georgia, serif;
  }
  .card {
    position: absolute;
    left: 80px;
    width: 732px;
    height: 428px;
    border-radius: 20px;
    overflow: hidden;
    box-shadow: 0 6px 14px rgba(0, 0, 0, 0.35);
  }
  .card-front {
    top: 130px;
    background: linear-gradient(135deg, var(--coral-light) 0%, var(--coral) 55%, var(--coral-deep) 100%);
    color: var(--ink);
    text-align: center;
  }
  .front-name {
    position: absolute;
    top: 172px;
    width: 100%;
    font-size: 29px;
    font-weight: 600;
    letter-spacing: 5px;
  }
  .front-phone {
    position: absolute;
    top: 213px;
    width: 100%;
    font-size: 18px;
    font-weight: 600;
    letter-spacing: 2px;
  }
  .front-email {
    position: absolute;
    top: 240px;
    width: 100%;
    font-size: 17px;
    font-weight: 600;
    letter-spacing: 1.5px;
  }
  .card-back {
    top: 645px;
    background: var(--card-black);
  }
  .wine-photo {
    position: absolute;
    right: 0;
    top: 0;
    width: 250px;
    height: 100%;
    z-index: 1;
    background:
      linear-gradient(90deg, var(--card-black) 0%, rgba(5, 5, 5, 0) 22%),
      radial-gradient(ellipse 70px 140px at 120px 200px, rgba(196, 40, 90, 0.85), rgba(122, 22, 48, 0.4) 60%, transparent 100%),
      linear-gradient(180deg, transparent 0%, transparent 72%, var(--wood) 82%, #3a1e0c 100%),
      linear-gradient(90deg, var(--card-black) 0%, #150608 40%, #1a0a0c 100%);
  }
  .back-brand {
    position: absolute;
    left: 64px;
    top: 200px;
    z-index: 2;
    display: flex;
    align-items: center;
    gap: 16px;
    color: var(--white);
    font-size: 28px;
    font-weight: 600;
    letter-spacing: 4px;
    white-space: nowrap;
  }
  .brand-dot {
    width: 30px;
    height: 30px;
    border-radius: 50%;
    background: var(--bordeaux);
  }
</style>
</head>
<body>
  <main class="canvas">
    <section class="card card-front" aria-label="Business card front">
      <h1 class="front-name">LORENZ HADWIGER</h1>
      <p class="front-phone">+438 271 905 316</p>
      <p class="front-email">KDORVAN4@QUILLPOST.NET</p>
    </section>

    <section class="card card-back" aria-label="Business card back">
      <div class="back-brand">
        <span class="brand-first">LORENZ</span>
        <span class="brand-dot"></span>
        <span class="brand-last">HADWIGER</span>
      </div>
      <div class="wine-photo" role="img" aria-label="Photo of red wine being poured from a bottle into a glass on a wooden table, with a cork beside it"></div>
    </section>
  </main>
</body>
</html>
```